Letterhead for 3 attorney Workers' Comp law firm

We are a 3 attorney law office. We specialize in Workers' Compensation. Our office represents workers who are injured on the job, and the estates of workers who are killed one the job.
When we started our office, we created our own letterhead & have been using it for years. We've just recently hired the 3rd attorney, and were going to just add his name to the letterhead, but have decided we wanted to get a professionally designed letterhead and business cards at this point.
We want something that looks clean and professional. It must look good in black and white because we often make multiple copies of our documents. We're hoping for a design that resonates confidence, reliability and experience.
The design must include the firm name: Dorrance & Pike, PLLC. We would like the PLLC to be small compared to the Dorrance & Pike graphic. We also want to incorporate the attorney names: Ulric Dorrance, Janet Pike, and Lyle Hagberg. Our current letterhead has our contact info in the footer at the bottom of the page. We like that design, but are open to the idea of having it at the top. We'll leave that at the discretion of the designer. Our contact info is as follows: 472 S. Larchmont Avenue, Suite 315 Bellingham, WA 98117 Phone: 360-514-2967, Fax: 360-521-6079, and our website: www.dorrancepike-law.example
Target Market(s)
Clients, courts, other legal offices, doctors offices. These are the people who see our letterhead most frequently. It's not so much for marketing purposes, mainly so that we have a professional image when sending out documents.
Industry/Entity Type
Law Firm
Contact Information for Business Card
On the back of the business card: it can be designed, or be a template for filling in appointment reminder information (i.e. date, time, etc)
Colors
Designer to choose colors to be used in the design.
Requirements
Must have
- Must have our firm name at the top.
- Must include the attorney names.
- Must have all of our contact information (can be at top or bottom - whatever looks best with the design)
Nice to have
- A strong, confident design
Should not have
- We don't want the design to be playful, cartoony or busy.

```html
<!DOCTYPE html>
<html lang="en">
<head>
<meta charset="utf-8">
<title>Dorrance &amp; Pike, PLLC — Letterhead</title>
<link href="https://fonts.googleapis.com/css2?family=Roboto+Slab:wght@300;400;700&display=swap" rel="stylesheet">
<style>
  :root {
    --paper: #ffffff;
    --page-edge: #d9d9d9;
    --ink: #1e1e1e;
    --ink-soft: #555555;
    --rule: #9a9a9a;
  }
  html, body {
    margin: 0;
    padding: 0;
    width: 934px;
    height: 1200px;
    overflow: hidden;
    background: var(--paper);
  }
  .letterhead {
    position: relative;
    width: 934px;
    height: 1200px;
    font-family: "Roboto Slab", Georgia, serif;
    color: var(--ink);
  }
  .sheet {
    position: absolute;
    left: 14px;
    top: 14px;
    width: 905px;
    height: 1172px;
    border: 1px solid var(--page-edge);
    box-sizing: border-box;
  }
  .masthead {
    position: absolute;
    left: 660px;
    top: 92px;
  }
  .firm-name {
    margin: 0;
    font-weight: 700;
    font-size: 33px;
    line-height: 38px;
    letter-spacing: -0.5px;
  }
  .firm-suffix {
    font-weight: 300;
    font-size: 25px;
    color: var(--ink-soft);
    letter-spacing: 0;
  }
  .attorneys {
    margin: 9px 0 0 2px;
    font-weight: 300;
    font-size: 14px;
    line-height: 18px;
  }
  .contact {
    margin: 7px 0 0 2px;
    padding: 0;
    list-style: none;
    font-weight: 300;
    font-size: 12.5px;
    line-height: 16px;
  }
  .contact li.web { margin-bottom: 6px; }
  .contact .label { font-weight: 700; }
  .footer {
    position: absolute;
    left: 94px;
    top: 1094px;
    width: 742px;
    display: flex;
    align-items: center;
    gap: 12px;
  }
  .footer-rule {
    flex: 0 0 392px;
    height: 1px;
    background: var(--rule);
  }
  .address {
    font-weight: 300;
    font-size: 12.5px;
    white-space: nowrap;
  }
</style>
</head>
<body>
  <div class="letterhead">
    <div class="sheet"></div>
    <header class="masthead">
      <h1 class="firm-name">Dorrance &amp;<br>Pike, <span class="firm-suffix">PLLC</span></h1>
      <p class="attorneys">Attorney: Ulric Dorrance,<br>Janet Pike, and Lyle Hagberg</p>
      <ul class="contact">
        <li class="web"><span class="label">w.</span> www.dorrancepike-law.example</li>
        <li><span class="label">t.</span> 360-514-2967</li>
        <li><span class="label">f.</span> 360-521-6079</li>
      </ul>
    </header>
    <footer class="footer">
      <span class="footer-rule"></span>
      <span class="address">472 S. Larchmont Avenue, Suite 315 Bellingham, WA 98117</span>
    </footer>
  </div>
</body>
</html>
```